Introducing Vessa – the virtual restaurant experience at home

Missing going out on dining at your favourite restaurant with your friends, then Vessa Dining is the answer.

While it may not be possible during the COVID-19 pandemic, or when restaurants return as booking opportunities will be hard to get, an innovative new concept gives people the chance to enjoy a virtual restaurant experience at home.

VESSA offers diners the ability to get the restaurant experience at home and restaurants to expand their dining rooms beyond the confines of social distancing

Vessa Dining is an app where you can book your favourite restaurant table, invite your friends and choose your menu and beverages. On the day the restaurant will come to your house, set your table, cook and serve you the menu you have chosen, serve you drinks and clean up, just like you where at the restaurant.

We are looking for 2 similar infographics to explain a process from 2 different perspective

The design needs to be simple, contemporary, imaginative and modern for this concept, it needs to be sophisticated, something that would represent an up-market to fine dining style of restaurant. The designs need to be easily understood using white space to separate the elements

Our preferred colour is attached along with our logos

Infographic 1 - Host Process
1. Host makes reservation at favourite restaurant at home on the Vessa Dining App
2. Select menus and invite guests
3. Confirm either single or shared payment options
4. Booking confirmed with restaurant
5. Host confirms on the App they the required equipment
6. Cook/server arrive 1 hour prior to guests, prepares and sets table
7. Guests arrive and cook/server offer dinks and serves meal
8. Cook/Server cleans up and finalises check with host

Infographic 2 - Restaurant Process
1. Host makes reservation and orders meal
2. Restaurant confirm reservation details
3. Restaurant prepares cuisine and arranges cook/serve waiter
4. Cook/server arrive 1 hour before guests, prepares and sets table
5. Cook/server cooks and serves meals and wine
6. Cook/Server cleans up and finalises check with host

Good Luck

```html
<!DOCTYPE html>
<html lang="en">
<head>
<meta charset="utf-8">
<title>Restaurant Process</title>
<link href="https://fonts.googleapis.com/css2?family=Open+Sans:wght@400;600&display=swap" rel="stylesheet">
<style>
  :root {
    --plum: #7a2270;
    --plum-line: #8e3d86;
    --panel: #f3f2f3;
    --note: #f3f3f5;
    --ink: #1d1d1f;
    --white: #ffffff;
  }
  * { box-sizing: border-box; margin: 0; padding: 0; }
  html, body { width: 1200px; height: 901px; overflow: hidden; background: var(--white); }
  body { font-family: "Open Sans", sans-serif; color: var(--ink); position: relative; }

  .frame { position: absolute; left: 36px; top: 44px; width: 1128px; height: 813px; border: 1px solid var(--plum-line); }

  .headline {
    position: absolute; left: 274px; top: 88px; width: 652px; height: 77px;
    border: 1px solid var(--plum-line); border-radius: 16px;
    display: flex; align-items: center; justify-content: center;
    color: var(--plum); font-weight: 600; font-size: 36px; line-height: 1;
    letter-spacing: -0.2px; white-space: nowrap;
  }

  .panel {
    position: absolute; left: 58px; top: 203px; width: 1085px; height: 610px;
    background: var(--panel); box-shadow: 0 10px 18px rgba(0,0,0,0.12);
  }
  .panel-border {
    position: absolute; left: 92px; top: 230px; width: 1017px; height: 556px;
    border: 1px solid var(--plum-line); border-radius: 16px;
  }
  .pill {
    position: absolute; left: 451px; top: 248px; width: 298px; height: 45px;
    background: var(--plum); border-radius: 23px;
    display: flex; align-items: center; justify-content: center;
    color: var(--white); font-size: 25px; font-weight: 400; white-space: nowrap;
  }

  .step {
    position: absolute; width: 245px; height: 194px;
    background: var(--white); border: 1px solid var(--plum-line); border-radius: 14px;
  }
  .step-number {
    position: absolute; left: 50%; top: -22px; transform: translateX(-50%);
    width: 42px; height: 42px; border-radius: 50%;
    background: var(--white); border: 1px solid var(--plum-line);
    display: flex; align-items: center; justify-content: center;
    color: var(--plum); font-size: 26px; font-weight: 600; letter-spacing: -0.5px;
  }
  .step-note {
    position: absolute; left: 14px; top: 19px; width: 217px; height: 55px;
    background: var(--note); border-radius: 9px;
    padding: 9px 8px 0 13px;
    font-size: 12px; line-height: 18.5px;
  }
  .step-art { position: absolute; border-radius: 4px; }

  .s1 { left: 162px; top: 337px; }
  .s2 { left: 478px; top: 337px; }
  .s3 { left: 794px; top: 337px; }
  .s4 { left: 162px; top: 576px; }
  .s5 { left: 478px; top: 576px; }
  .s6 { left: 794px; top: 576px; }

  .s1 .step-art { left: 71px; top: 84px; width: 103px; height: 104px; border-radius: 50%;
    background: radial-gradient(circle, #e4e4e6 0%, #eceef0 60%, #f7f7f8 100%); }
  .s2 .step-art { left: 50px; top: 84px; width: 142px; height: 104px;
    background: linear-gradient(90deg, #ececee 0%, #ececee 45%, #a55aa0 46%, #c9b9c3 100%); }
  .s3 .step-art { left: 39px; top: 84px; width: 167px; height: 104px;
    background: linear-gradient(90deg, #b25fad 0%, #c98a55 30%, #8fc7ec 55%, #cde6f6 80%, #ecd7ea 100%); }
  .s4 .step-art { left: 37px; top: 84px; width: 172px; height: 104px;
    background: linear-gradient(90deg, #b25fad 0%, #d9d6d6 25%, #b9a79f 45%, #8fc7ec 60%, #cde6f6 85%, #b25fad 100%); }
  .s5 .step-art { left: 36px; top: 84px; width: 173px; height: 104px;
    background: linear-gradient(90deg, #e6ecf5 0%, #d8e3ef 50%, #8fc7ec 60%, #cde6f6 85%, #b25fad 100%); }
  .s6 .step-art { left: 32px; top: 84px; width: 180px; height: 104px;
    background: linear-gradient(90deg, #b25fad 0%, #8fc7ec 30%, #cde6f6 55%, #8fc7ec 75%, #b25fad 100%); }
</style>
</head>
<body>
  <div class="frame"></div>
  <h1 class="headline">Infographic 2 - Restaurant Process</h1>

  <div class="panel"></div>
  <div class="panel-border"></div>
  <div class="pill">Restaurant Process</div>

  <section class="step s1">
    <div class="step-number">01</div>
    <p class="step-note">Host makes reservation and orders meal</p>
    <div class="step-art" role="img" aria-label="Illustration of a person browsing restaurant listings on a large phone screen"></div>
  </section>

  <section class="step s2">
    <div class="step-number">02</div>
    <p class="step-note">Restaurant confirm reservation details</p>
    <div class="step-art" role="img" aria-label="Illustration of a phone confirming a booking beside a restaurant counter with a menu board"></div>
  </section>

  <section class="step s3">
    <div class="step-number">03</div>
    <p class="step-note">Restaurant prepares cuisine and arranges cook/serve&nbsp; waiter</p>
    <div class="step-art" role="img" aria-label="Illustration of a chef packing food in a kitchen and a waiter preparing a table"></div>
  </section>

  <section class="step s4">
    <div class="step-number">04</div>
    <p class="step-note">Cook/server cooks and serves meals and wine</p>
    <div class="step-art" role="img" aria-label="Illustration of a cook at the stove and a server bringing a covered dish to a table"></div>
  </section>

  <section class="step s5">
    <div class="step-number">05</div>
    <p class="step-note">Cook/server Arrive 1 Hour Prior To Guests, Prepares And Sets Table</p>
    <div class="step-art" role="img" aria-label="Illustration of a scooter travelling across the city and a server setting a table with flowers"></div>
  </section>

  <section class="step s6">
    <div class="step-number">06</div>
    <p class="step-note">Cook/server Cleans Up And Finalises Check With Host</p>
    <div class="step-art" role="img" aria-label="Illustration of diners paying the server at a table while the floor is mopped"></div>
  </section>
</body>
</html>
```